Catalogue Front Cover Design

To design the front cover of a toiletries catalogue. Open artwork required from the winner as detail content will not be correct until day of printing.
Updates

Updated Requirement : - Top Logo Style & Position and bottom text Style & Postion to remain unchanged.

Target Market(s)

Target Customers : Chain stores,Pharmacies and Local Shops.

Requirements
Must have
• Must be bright and vibrant, must contain the detail as per example.
Nice to have
• Cover Items are Promotion Items with big discounts so need to stand out. Products used will change on day so use any low res picture for visualisation.
Should not have
• Images of ladies/men

```html
<!DOCTYPE html>
<html lang="en">
<head>
<meta charset="utf-8">
<title>Kestrel Toiletries – Special Promotions Catalogue Cover</title>
<link rel="stylesheet" href="https://fonts.googleapis.com/css2?family=Jost:wght@400;600&family=Arimo:wght@400;700&display=swap">
<style>
  :root {
    --sky: #dbeefc;
    --orange: #ff671f;
    --red: #ff0000;
    --mint: #62ffa8;
    --white: #ffffff;
    --ink: #000000;
  }
  html, body {
    margin: 0;
    padding: 0;
    overflow: hidden;
    background: var(--white);
  }
  .cover {
    position: relative;
    width: 873px;
    height: 1200px;
    overflow: hidden;
    background: var(--sky);
  }
  .cover-art {
    position: absolute;
    inset: 0;
    display: block;
  }
  .bubble-orange { fill: var(--orange); }
  .bubble-red { fill: var(--red); }
  .bubble-mint { fill: var(--mint); }
  .brand-name {
    font-family: "Jost", sans-serif;
    font-weight: 400;
    font-size: 46px;
    fill: var(--white);
  }
  .brand-address {
    font-family: "Jost", sans-serif;
    font-weight: 600;
    font-size: 16.5px;
    letter-spacing: -0.6px;
    fill: var(--white);
  }
  .offer-price {
    font-family: "Arimo", sans-serif;
    font-weight: 700;
    font-size: 70px;
    fill: var(--red);
  }
  .offer-detail {
    font-family: "Arimo", sans-serif;
    font-weight: 700;
    font-size: 21px;
    letter-spacing: -1px;
    fill: var(--white);
  }
  .headline {
    font-family: "Jost", sans-serif;
    font-weight: 400;
    font-size: 93px;
    fill: var(--white);
  }
  .footer-band { fill: var(--mint); }
  .footer-contact {
    font-family: "Arimo", sans-serif;
    font-weight: 700;
    font-size: 15.5px;
    fill: var(--ink);
  }
  .footer-hours {
    font-family: "Arimo", sans-serif;
    font-weight: 400;
    font-size: 15.5px;
    fill: var(--ink);
  }
  .footer-web {
    font-family: "Arimo", sans-serif;
    font-weight: 700;
    font-size: 25px;
    fill: var(--white);
  }
</style>
</head>
<body>
<main class="cover">
  <svg class="cover-art" width="873" height="1200" viewBox="0 0 873 1200" xmlns="http://www.w3.org/2000/svg">
    <!-- Brand bubble -->
    <circle class="bubble-orange" cx="729" cy="95" r="204"/>
    <text class="brand-name" x="562" y="134">Kestrel</text>
    <g class="brand-address">
      <text x="738" y="55">Kestrel Toiletries</text>
      <text x="738" y="74">Unit 7</text>
      <text x="738" y="93">Mill Lane</text>
      <text x="738" y="112">Hartwell</text>
      <text x="738" y="131">HW4 2PL</text>
      <text x="738" y="150">England</text>
    </g>

    <!-- Bottom-left bubble -->
    <circle class="bubble-orange" cx="73" cy="915" r="162"/>

    <!-- Price offer bubble -->
    <circle class="bubble-mint" cx="212" cy="540" r="121"/>
    <ellipse class="bubble-orange" cx="335" cy="451" rx="43" ry="40"/>
    <text class="offer-price" x="144" y="541" textLength="131" lengthAdjust="spacingAndGlyphs">8.99</text>
    <text class="offer-detail" x="167" y="567" textLength="93" lengthAdjust="spacingAndGlyphs">RRP: 2.69</text>
    <text class="offer-detail" x="167" y="591" textLength="88" lengthAdjust="spacingAndGlyphs">POR 10%</text>

    <!-- Headline bubble -->
    <ellipse class="bubble-red" cx="577" cy="682" rx="245" ry="222"/>
    <text class="headline" x="354" y="663" textLength="302" lengthAdjust="spacingAndGlyphs">SPECIAL</text>
    <text class="headline" x="354" y="749" textLength="451" lengthAdjust="spacingAndGlyphs">PROMOTIONS</text>

    <!-- Footer -->
    <rect class="footer-band" x="3" y="1053" width="870" height="147"/>
    <text class="footer-contact" x="43" y="1085">SALES TEL: 0700 100 2000</text>
    <text class="footer-contact" x="270" y="1085">FAX: 0700 100 2001</text>
    <text class="footer-hours" x="43" y="1110">Telesales - Lines open 8am - 4pm orders must be received by 3pm</text>
    <text class="footer-web" x="562" y="1088" textLength="283" lengthAdjust="spacingAndGlyphs">www.kestreltoiletries.com</text>
  </svg>
</main>
</body>
</html>
```